App Design - Job Lantern Quokka

We require an App Design for our new App called 'Lantern Quokka'. This app is essentially an assistant to help Users prepare for job interviews, to help them get hired. <br/><br/>Users who download the App can view common Questions and Answers, save their favourite responses and also view common Interview Tips. <br/><br/>The vision for our App is for Users who are preparing for an interview (1 week before, 1 day before, even 1 hour before), are able to download, view and educate themselves on common questions and responses, and then be confident to land the job. <br/><br/>Our team has developed wireframes to help highlight what each screen should do and include. Please see attached document, which also highlights key requirements for the experience. Feel free to add/remove/edit what you see on these wireframes. Our preference is that you use Adobe XD please.<br/><br/>In terms of design guidelines, we want the experience to be simple, intuitive and 'memorable' to help Users to remember the questions/responses when they are in the interview. <br/><br/>The final design should communicate 'neat and clean professionalism'; we like the design of: marlo vane com au<br/><br/>Thank you for reading! Good luck !

Target Market(s)

Professional job seekers

Font styles to use
Sans Serif

Colors

Designer to choose colors to be used in the design.

Requirements
Must have
• Please see my PlanHive_UX file that I have uploaded
Nice to have
• Could you also please include some ideas on how we can incorporate Advertising into the app screens

```html
<!DOCTYPE html>
<html lang="en">
<head>
<meta charset="utf-8">
<title>Lantern Quokka — App Screens</title>
<link href="https://fonts.googleapis.com/css2?family=Poppins:wght@400;500;600;700&family=Open+Sans:wght@400;600;700&display=swap" rel="stylesheet">
<style>
  :root{
    --blue:#5572f7;
    --blue-soft:#dfe4fd;
    --pink:#f1589b;
    --teal:#2fd3c0;
    --amber:#f7c948;
    --ink:#282d44;
    --muted:#868b9c;
    --faint:#c4c8d3;
    --frame:#d8dce6;
    --screen:#f4f5f8;
    --card:#ffffff;
    --canvas:#ffffff;
  }
  *{box-sizing:border-box;margin:0;padding:0}
  html,body{width:1200px;height:946px;overflow:hidden;background:var(--canvas)}
  body{position:relative;font-family:"Open Sans",sans-serif;color:var(--ink)}
  .backdrop{position:absolute;left:0;top:0}
  .phone{position:absolute;width:157px;height:335px;border:3px solid var(--frame);border-radius:22px;background:var(--screen);overflow:hidden}
  .abs{position:absolute}
  .art{position:absolute;border-radius:50%}
  .app-header{position:absolute;left:0;top:0;width:100%;height:38px;background:var(--card)}
  .brand{position:absolute;top:20px;left:0;width:100%;display:flex;justify-content:center;align-items:center;gap:3px;font-family:"Poppins",sans-serif;font-weight:600;font-size:6.4px;color:var(--ink)}
  .brand-mark{width:6px;height:6px;background:var(--blue);border-radius:1px}
  .back{position:absolute;left:10px;top:17px;font-size:10px;color:var(--ink);font-family:"Poppins",sans-serif}
  .screen-title{position:absolute;top:20px;left:0;width:100%;text-align:center;font-family:"Poppins",sans-serif;font-weight:600;font-size:7.5px}
  .banner{position:absolute;left:0;top:38px;width:100%;height:30px;background:var(--screen)}
  .banner-title{position:absolute;left:11px;top:6px;font-family:"Poppins",sans-serif;font-weight:500;font-size:7.4px;line-height:9.5px;color:#7d8296}
  .banner-art{position:absolute;right:6px;top:1px;width:38px;height:30px;border-radius:8px;background:linear-gradient(135deg,#e8ecff,#b9c4f5)}
  .folder-art{position:absolute;right:6px;top:2px;width:33px;height:28px;border-radius:4px;background:linear-gradient(180deg,#fbd46a,#f3a94a)}
  .hint{position:absolute;left:10px;font-size:4.2px;color:var(--muted)}
  .section{position:absolute;left:10px;font-family:"Poppins",sans-serif;font-weight:600;font-size:7.8px;color:var(--ink)}
  .card{position:absolute;background:var(--card);border-radius:3px}
  .q{font-size:5.1px;line-height:8px;color:var(--ink)}
  .q-lg{font-size:5.7px;line-height:8.3px;color:#3b4058}
  .crumb{font-size:3.6px;color:var(--muted)}
  .meta{font-size:3.4px;font-weight:700;color:#4a4f66;display:flex;align-items:center;gap:2px}
  .chev{position:absolute;right:8px;font-size:7px;color:var(--faint)}
  .tag{position:absolute;left:10px;top:75px;height:13px;border-radius:1.5px;color:#fff;font-family:"Poppins",sans-serif;font-weight:500;font-size:4.8px;line-height:13px;padding:0 7px}
  .tag.pink{background:var(--pink)}
  .tag.blue{background:var(--blue)}
  .tag-row{position:absolute;left:0;top:68px;width:100%;height:28px;background:var(--screen)}
  .list-area{position:absolute;left:0;top:96px;width:100%;height:240px;background:#f0f1f5}
  .cat{position:absolute;left:10px;width:137px;height:27px;background:var(--card);border-radius:3px}
  .cat-icon{position:absolute;left:2px;top:4px;width:18px;height:19px;border-radius:3px;background:#eceef3}
  .cat-name{position:absolute;left:23px;top:6px;font-family:"Poppins",sans-serif;font-weight:500;font-size:6.4px}
  .cat-sub{position:absolute;left:23px;top:16px;font-size:3.1px;color:var(--muted)}
  .corner{position:absolute;right:2px;top:2px;width:0;height:0;border-top:5px solid;border-left:5px solid transparent}
  .btn-ghost{position:absolute;height:13px;padding:0 13px;background:var(--card);border-radius:2px;font-family:"Poppins",sans-serif;font-weight:600;font-size:5px;line-height:13px}
  .cta{position:absolute;left:43px;width:68px;height:21px;border-radius:11px;text-align:center;line-height:21px;font-family:"Poppins",sans-serif;font-weight:600;font-size:5.6px}
  .hero-title{position:absolute;left:0;width:100%;text-align:center;font-family:"Poppins",sans-serif;font-weight:700;font-size:8.6px}
  .hero-sub{position:absolute;left:18px;width:115px;text-align:center;font-size:5.2px;line-height:8px}
  .hero-brand{position:absolute;left:11px;top:42px;display:flex;align-items:center;gap:4px;font-family:"Poppins",sans-serif;font-weight:600;font-size:10px}
  .hero-brand .brand-mark{width:9px;height:9px}
  .resp-title{position:absolute;left:10px;top:9px;font-family:"Poppins",sans-serif;font-weight:600;font-size:5px}
  .resp-bar{position:absolute;left:10px;top:17px;width:7px;height:1.5px;background:var(--pink);border-radius:1px}
  .resp-text{position:absolute;left:10px;top:26px;width:118px;font-size:4.1px;line-height:7.4px;color:var(--muted)}
  .mark{position:absolute;right:9px;top:8px}
  .search-bar{position:absolute;left:10px;top:43px;width:137px;height:15px;background:#f0f1f5;border-radius:2px;font-size:4.6px;color:var(--muted);line-height:15px;padding-left:16px}
  .search-bar svg{position:absolute;left:5px;top:4px}
  .delete{position:absolute;left:8px;font-size:3.4px;font-weight:700;color:#4a4f66;display:flex;align-items:center;gap:2px}
  .delete i{display:inline-block;width:5px;height:5px;border:0.7px solid var(--pink);border-radius:50%}
  .caption{position:absolute;width:220px;text-align:center;font-family:"Poppins",sans-serif;font-weight:600;font-size:10.6px;line-height:14px;color:var(--ink)}
  .caption .sub{display:block;color:#a3a8b8}
  .caption .sub.pale{color:#dde0e7}
  .nav{position:absolute;left:0;bottom:0;width:100%;height:30px;background:var(--card);border-radius:0 0 18px 18px}
  .nav-item{position:absolute;top:8px;font-size:3.6px;text-align:center;width:30px}
</style>
</head>
<body>

<svg class="backdrop" width="1200" height="946" aria-hidden="true">
  <path d="M0 0 H362 L210 250 Q170 330 0 352 Z" fill="var(--blue)"/>
</svg>

<!-- Landing v1 -->
<div class="phone" style="left:52px;top:86px;background:#fff">
  <svg class="abs" style="left:0;top:0" width="151" height="150" aria-hidden="true">
    <path d="M0 0 H151 V60 Q130 70 128 110 Q120 145 75 140 Q20 135 0 120 Z" fill="var(--blue)"/>
  </svg>
  <div class="hero-brand" style="color:#fff"><span class="brand-mark" style="background:#fff"></span>LanternQuokka</div>
  <div class="art" role="img" aria-label="Illustration of a woman working at a laptop with idea bulb and heart icons" style="left:20px;top:90px;width:115px;height:90px;border-radius:45% 55% 50% 50%;background:linear-gradient(160deg,#c9d2fb,#7f95f5)"></div>
  <div class="hero-title" style="top:207px">Job Interview Questions</div>
  <div class="hero-sub" style="top:225px;color:var(--muted)">Your guide to the most common interview questions, and the best responses to help you get hired!</div>
  <div class="cta" style="top:272px;background:var(--blue);color:#fff">Get started</div>
</div>

<!-- Landing v2 -->
<div class="phone" style="left:240px;top:86px;background:#fff">
  <svg class="abs" style="left:0;top:0" width="151" height="335" aria-hidden="true">
    <path d="M0 80 Q40 95 75 95 Q110 90 125 70 Q140 60 151 65 V335 H0 Z" fill="var(--blue)"/>
  </svg>
  <div class="hero-brand" style="color:var(--ink)"><span class="brand-mark"></span>LanternQuokka</div>
  <div class="art" role="img" aria-label="Illustration of a woman at a laptop beside a plant, heart and idea bulb" style="left:18px;top:100px;width:118px;height:95px;border-radius:40%;background:linear-gradient(150deg,#8ea0fb,#3f5ad8)"></div>
  <div class="hero-title" style="top:210px;color:#fff">Job Interview Questions</div>
  <div class="hero-sub" style="top:229px;color:#eef1ff">Your guide to the most common interview questions, and the best responses to help you get hired!</div>
  <div class="cta" style="top:270px;background:#fff;color:var(--blue)">Get started</div>
</div>

<!-- Menu -->
<div class="phone" style="left:428px;top:86px">
  <div class="app-header">
    <div class="brand" style="justify-content:flex-start;left:10px"><span class="brand-mark"></span>LanternQuokka</div>
    <svg class="abs" style="left:119px;top:20px" width="8" height="8" aria-hidden="true"><circle cx="3.3" cy="3.3" r="2.5" fill="none" stroke="var(--ink)" stroke-width="1.1"/><path d="M5.2 5.2 L7.5 7.5" stroke="var(--ink)" stroke-width="1.1"/></svg>
    <div class="abs" style="left:135px;top:16px;width:11px;height:11px;border-radius:50%;background:var(--blue-soft);border:1px solid var(--blue)"></div>
  </div>
  <div class="hint" style="top:46px;font-weight:600;color:#6b7085">We will help you to face job interviews with more confidence!</div>
  <div class="hint" style="top:54px">below there's some categories where you can start</div>
  <div class="section" style="top:74px">Categories</div>
  <div class="card" style="left:10px;top:90px;width:66px;height:60px">
    <div class="art" role="img" aria-label="Astronaut illustration" style="left:20px;top:9px;width:26px;height:24px;background:linear-gradient(135deg,#e3e8ff,#9fb0f4)"></div>
    <div class="abs" style="left:0;top:40px;width:100%;text-align:center;font-size:4.4px;line-height:5.6px;font-weight:600">View Questions &amp;<br>Responses</div>
  </div>
  <div class="card" style="left:81px;top:90px;width:66px;height:60px">
    <div class="abs" role="img" aria-label="Folder with briefcase illustration" style="left:21px;top:11px;width:24px;height:22px;border-radius:3px;background:linear-gradient(180deg,#fbd46a,#f3a94a)"></div>
    <div class="abs" style="left:0;top:43px;width:100%;text-align:center;font-size:4.4px;font-weight:600">Interview Tips</div>
  </div>
  <div class="section" style="top:160px">Most searched</div>
  <div class="card" style="left:10px;top:176px;width:137px;height:68px">
    <div class="crumb abs" style="left:8px;top:7px">View Questions &amp; Responses › Behavioural</div>
    <div class="q abs" style="left:8px;top:18px;width:124px">Give me an example of a new idea or initiative you have suggested to your manager. How did you implement your idea?</div>
    <div class="meta abs" style="left:8px;top:55px"><svg width="4" height="6"><path d="M0 0H4V6L2 4.5L0 6Z" fill="var(--blue)"/></svg>23 SAVES</div>
    <div class="meta abs" style="right:8px;top:55px"><svg width="6" height="6"><circle cx="1.2" cy="3" r="1" fill="none" stroke="#4a4f66" stroke-width=".6"/><circle cx="4.8" cy="1.2" r="1" fill="none" stroke="#4a4f66" stroke-width=".6"/><circle cx="4.8" cy="4.8" r="1" fill="none" stroke="#4a4f66" stroke-width=".6"/><path d="M2 2.6L4 1.5M2 3.4L4 4.5" stroke="#4a4f66" stroke-width=".5"/></svg>SHARE</div>
  </div>
  <div class="card" style="left:10px;top:249px;width:137px;height:60px">
    <div class="crumb abs" style="left:8px;top:7px">View Questions &amp; Responses › Behavioural</div>
    <div class="q abs" style="left:8px;top:18px;width:124px">Give me an example of a time when you made a mistake or didn't deliver on expectations, what happened? What did you learn?</div>
  </div>
  <div class="nav">
    <div class="nav-item" style="left:30px;color:var(--blue)"><svg width="5" height="9" style="display:block;margin:0 auto 2px"><path d="M2.5 0L5 3L3.5 9H1.5L0 3Z" fill="none" stroke="var(--blue)" stroke-width=".8"/></svg>Home</div>
    <div nav class="nav-item" style="left:91px;color:var(--ink)"><svg width="6" height="8" style="display:block;margin:0 auto 2px"><path d="M.5 .5H5.5V7.5L3 5.8L.5 7.5Z" fill="none" stroke="var(--ink)" stroke-width=".8"/></svg>Saved</div>
  </div>
</div>

<!-- Selection menu -->
<div class="phone" style="left:616px;top:86px">
  <div class="app-header"><div class="back">‹</div><div class="brand"><span class="brand-mark"></span>LanternQuokka</div></div>
  <div class="banner"><div class="banner-title">View Questions &amp;<br>Responses</div><div class="banner-art" role="img" aria-label="Astronaut holding a flag illustration"></div></div>
  <div class="list-area" style="top:68px;background:#f0f1f5"></div>
  <div class="hint" style="top:80px;color:#6b7085">Select your question category</div>
  <div class="cat" style="top:88px"><div class="cat-icon" role="img" aria-label="Line icon of people"></div><div class="cat-name">Behavioural</div><div class="cat-sub">Pellentesque quis neque ut sapien fringilla iaculis ege inc...</div><span class="corner" style="border-top-color:var(--pink)"></span></div>
  <div class="cat" style="top:120px"><div class="cat-icon" role="img" aria-label="Line icon of a signpost"></div><div class="cat-name">Situational</div><div class="cat-sub">Pellentesque quis neque ut sapien fringilla iaculis ege inc...</div><span class="corner" style="border-top-color:var(--amber)"></span></div>
  <div class="cat" style="top:152px"><div class="cat-icon" role="img" aria-label="Line icon of a raised hand"></div><div class="cat-name">Motivational</div><div class="cat-sub">Pellentesque quis neque ut sapien fringilla iaculis ege inc...</div><span class="corner" style="border-top-color:var(--teal)"></span></div>
  <div class="cat" style="top:185px"><div class="cat-icon" role="img" aria-label="Line icon of a target"></div><div class="cat-name">Technical</div><div class="cat-sub">Pellentesque quis neque ut sapien fringilla iaculis ege inc...</div><span class="corner" style="border-top-color:var(--teal)"></span></div>
  <div class="btn-ghost" style="left:99px;top:222px">View all</div>
  <div class="section" style="top:256px">Most searched</div>
  <div class="card" style="left:10px;top:272px;width:137px;height:60px;opacity:.75">
    <div class="crumb abs" style="left:8px;top:7px">View Questions &amp; Responses › Behavioural</div>
    <div class="q-lg abs" style="left:8px;top:17px;width:124px;color:#6b7085">Give me an example of a new idea or initiative you have suggested to your manager. How did you implement your...</div>
  </div>
</div>

<!-- View list -->
<div class="phone" style="left:804px;top:86px">
  <div class="app-header"><div class="back">‹</div><div class="brand"><span class="brand-mark"></span>LanternQuokka</div></div>
  <div class="banner"><div class="banner-title">View Questions &amp;<br>Responses</div><div class="banner-art" role="img" aria-label="Astronaut holding a flag illustration"></div></div>
  <div class="tag-row"></div>
  <div class="tag pink" style="top:73px">Behavioural</div>
  <div class="btn-ghost" style="left:103px;top:73px;font-weight:500;font-size:4.6px;padding:0 8px">Sort by ⌄</div>
  <div class="list-area"></div>
  <div class="card" style="left:10px;top:100px;width:137px;height:45px"><div class="q abs" style="left:8px;top:6px;width:112px">1. Give me an example of a new idea or initiative you have suggested to your manager. How did you implement your idea?</div><span class="chev" style="top:17px">›</span></div>
  <div class="card" style="left:10px;top:152px;width:137px;height:45px"><div class="q abs" style="left:8px;top:6px;width:112px">2. Give me an example of a time when you made a mistake or didn't deliver on expectations, what happened? What did you learn?</div><span class="chev" style="top:17px">›</span></div>
  <div class="card" style="left:10px;top:203px;width:137px;height:31px"><div class="q abs" style="left:8px;top:7px;width:112px">3. How would your colleagues describe you in three words?</div><span class="chev" style="top:10px">›</span></div>
  <div class="card" style="left:10px;top:240px;width:137px;height:31px"><div class="q abs" style="left:8px;top:7px;width:112px">4. What parts of your current role frustrate you?</div><span class="chev" style="top:10px">›</span></div>
  <div class="card" style="left:10px;top:277px;width:137px;height:31px"><div class="q abs" style="left:8px;top:7px;width:112px">5. What steps would you take to make an important decision on the job?</div><span class="chev" style="top:10px">›</span></div>
</div>

<!-- Open question -->
<div class="phone" style="left:992px;top:86px">
  <div class="app-header"><div class="back">‹</div><div class="brand"><span class="brand-mark"></span>LanternQuokka</div></div>
  <div class="banner"><div class="banner-title">View Questions &amp;<br>Responses</div><div class="banner-art" role="img" aria-label="Astronaut holding a flag illustration"></div></div>
  <div class="tag-row"></div>
  <div class="tag pink" style="top:73px">Behavioural</div>
  <div class="abs" style="left:0;top:96px;width:100%;height:56px;background:#fff"></div>
  <div class="q abs" style="left:14px;top:104px;width:123px;text-align:center">1. Give me an example of a new idea or initiative you have suggested to your manager. How did you implement your idea?</div>
  <div class="meta abs" style="left:9px;top:144px"><svg width="6" height="6"><circle cx="1.2" cy="3" r="1" fill="none" stroke="#4a4f66" stroke-width=".6"/><circle cx="4.8" cy="1.2" r="1" fill="none" stroke="#4a4f66" stroke-width=".6"/><circle cx="4.8" cy="4.8" r="1" fill="none" stroke="#4a4f66" stroke-width=".6"/><path d="M2 2.6L4 1.5M2 3.4L4 4.5" stroke="#4a4f66" stroke-width=".5"/></svg>SHARE</div>
  <div class="abs" style="left:121px;top:140px;font-size:7px;color:var(--faint)">‹</div>
  <div class="abs" style="left:139px;top:140px;font-size:7px;color:var(--ink)">›</div>
  <div class="list-area" style="top:152px"></div>
  <div class="card" style="left:10px;top:168px;width:137px;height:56px"><div class="resp-title">Response 1</div><div class="resp-bar"></div><svg class="mark" width="5" height="6"><path d="M0 0H5V6L2.5 4.4L0 6Z" fill="var(--blue)"/></svg><div class="resp-text">I was attracted to this organisation because of the culture and what I have read on Hivepost Reviews. I was very impressed</div></div>
  <div class="abs" style="left:102px;top:160px;height:11px;padding:0 8px;background:#fff;border-radius:6px;font-size:4.6px;font-weight:700;line-height:11px;box-shadow:0 1px 3px rgba(40,45,68,.12)">Saved!</div>
  <div class="card" style="left:10px;top:231px;width:137px;height:56px"><div class="resp-title">Response 2</div><div class="resp-bar"></div><svg class="mark" width="5" height="6"><path d="M0 0H5V6L2.5 4.4L0 6Z" fill="var(--blue)"/></svg><div class="resp-text">I was attracted to this organisation because of the culture and what I have read on Hivepost Reviews. I was very impressed</div></div>
  <div class="card" style="left:10px;top:294px;width:137px;height:40px;opacity:.7"><div class="resp-title" style="color:var(--muted)">Response 3</div><div class="resp-bar" style="opacity:.5"></div><svg class="mark" width="5" height="6"><path d="M.4 .4H4.6V5.4L2.5 4L.4 5.4Z" fill="none" stroke="var(--muted)" stroke-width=".6"/></svg><div class="resp-text" style="color:var(--faint)">I was attracted to this organisation because of the</div></div>
</div>

<!-- Captions row 1 -->
<div class="caption" style="left:20px;top:437px">Landing Screen<span class="sub pale">Version 1</span></div>
<div class="caption" style="left:208px;top:437px">Landing Screen<span class="sub pale">Version 2</span></div>
<div class="caption" style="left:396px;top:437px">Menu Screen</div>
<div class="caption" style="left:578px;top:437px">Views questions<span class="sub">Selection Menú</span></div>
<div class="caption" style="left:776px;top:437px">Views questions<span class="sub">View list</span></div>
<div class="caption" style="left:974px;top:437px">Views questions<span class="sub">Open question</span></div>

<!-- Tips selection -->
<div class="phone" style="left:50px;top:508px">
  <div class="app-header"><div class="back">‹</div><div class="brand"><span class="brand-mark"></span>LanternQuokka</div></div>
  <div class="banner"><div class="banner-title" style="top:10px">Interview Tips</div><div class="folder-art" role="img" aria-label="Folder with briefcase illustration"></div></div>
  <div class="list-area" style="top:68px"></div>
  <div class="hint" style="top:80px;color:#6b7085">Select your interview tip category</div>
  <div class="cat" style="top:88px"><div class="cat-icon" role="img" aria-label="Line icon of a notepad"></div><div class="cat-name">Tips for before the interview</div><div class="cat-sub">Pellentesque quis neque ut sapien fringilla iaculis ege inc...</div><span class="corner" style="border-top-color:var(--blue)"></span></div>
  <div class="cat" style="top:120px"><div class="cat-icon" role="img" aria-label="Line icon of a person at a desk"></div><div class="cat-name">Tips for during the interview</div><div class="cat-sub">Pellentesque quis neque ut sapien fringilla iaculis ege inc...</div><span class="corner" style="border-top-color:var(--teal)"></span></div>
  <div class="cat" style="top:153px"><div class="cat-icon" role="img" aria-label="Line icon of a light bulb"></div><div class="cat-name">Tips for after the interview</div><div class="cat-sub">Pellentesque quis neque ut sapien fringilla iaculis ege inc...</div><span class="corner" style="border-top-color:var(--teal)"></span></div>
  <div class="btn-ghost" style="left:97px;top:203px">View all</div>
  <div class="section" style="top:236px">Most searched</div>
  <div class="card" style="left:10px;top:252px;width:137px;height:64px">
    <div class="crumb abs" style="left:8px;top:7px">View Questions &amp; Responses › Behavioural</div>
    <div class="q-lg abs" style="left:8px;top:17px;width:124px">Give me an example of a new idea or initiative you have suggested to your manager. How did you implement your...</div>
    <div class="meta abs" style="left:8px;top:53px;color:var(--muted)"><svg width="4" height="6"><path d="M0 0H4V6L2 4.5L0 6Z" fill="var(--blue)"/></svg>23 SAVES</div>
    <div class="meta abs" style="right:8px;top:53px;color:var(--muted)">SHARE</div>
  </div>
</div>

<!-- View tips -->
<div class="phone" style="left:240px;top:508px">
  <div class="app-header"><div class="back">‹</div><div class="brand"><span class="brand-mark"></span>LanternQuokka</div></div>
  <div class="banner"><div class="banner-title" style="top:10px">Interview Tips</div><div class="folder-art" role="img" aria-label="Folder with briefcase illustration"></div></div>
  <div class="tag-row"></div>
  <div class="tag blue" style="top:73px">Tips for before the interview</div>
  <div class="list-area"></div>
  <div class="card" style="left:10px;top:100px;width:137px;height:32px"><div class="q abs" style="left:8px;top:8px;width:112px">1. Start by researching the company and your interviewers</div><span class="chev" style="top:11px">›</span></div>
  <div class="card" style="left:10px;top:137px;width:137px;height:32px"><div class="q abs" style="left:8px;top:8px;width:112px">2. Practice your answers to common interview questions</div><span class="chev" style="top:11px">›</span></div>
  <div class="card" style="left:10px;top:174px;width:137px;height:22px"><div class="q abs" style="left:8px;top:7px;width:112px">3. Re-read the job description</div><span class="chev" style="top:6px">›</span></div>
  <div class="card" style="left:10px;top:202px;width:137px;height:31px"><div class="q abs" style="left:8px;top:7px;width:112px">4. What parts of your current role frustrate you?</div><span class="chev" style="top:10px">›</span></div>
  <div class="card" style="left:10px;top:239px;width:137px;height:31px"><div class="q abs" style="left:8px;top:7px;width:112px">5. Recruit a friend to practice answering questions</div><span class="chev" style="top:10px">›</span></div>
  <div class="card" style="left:10px;top:276px;width:137px;height:22px"><div class="q abs" style="left:8px;top:7px;width:112px">6. Prepare a list of references</div><span class="chev" style="top:6px">›</span></div>
  <div class="card" style="left:10px;top:304px;width:137px;height:30px;opacity:.5"><div class="q abs" style="left:8px;top:7px;width:112px;color:var(--muted)">7. Be prepared with examples of your work</div></div>
</div>

<!-- Hint 7 -->
<div class="phone" style="left:428px;top:508px">
  <div class="app-header"><div class="back">‹</div><div class="brand"><span class="brand-mark"></span>LanternQuokka</div></div>
  <div class="banner"><div class="banner-title" style="top:10px">Interview Tips</div><div class="folder-art" role="img" aria-label="Folder with briefcase illustration"></div></div>
  <div class="tag-row"></div>
  <div class="tag blue" style="top:73px">Tips for before the interview</div>
  <div class="abs" style="left:0;top:96px;width:100%;height:44px;background:#fff"></div>
  <div class="q abs" style="left:0;top:107px;width:100%;text-align:center">7. Be prepared with examples of your work</div>
  <div class="meta abs" style="left:9px;top:127px"><svg width="6" height="6"><circle cx="1.2" cy="3" r="1" fill="none" stroke="#4a4f66" stroke-width=".6"/><circle cx="4.8" cy="1.2" r="1" fill="none" stroke="#4a4f66" stroke-width=".6"/><circle cx="4.8" cy="4.8" r="1" fill="none" stroke="#4a4f66" stroke-width=".6"/><path d="M2 2.6L4 1.5M2 3.4L4 4.5" stroke="#4a4f66" stroke-width=".5"/></svg>SHARE</div>
  <div class="abs" style="left:121px;top:123px;font-size:7px;color:var(--faint)">‹</div>
  <div class="abs" style="left:139px;top:123px;font-size:7px;color:var(--ink)">›</div>
  <div class="list-area" style="top:140px"></div>
  <div class="card" style="left:10px;top:148px;width:137px;height:82px">
    <div class="resp-title">Tips</div><div class="resp-bar" style="background:var(--blue)"></div>
    <svg class="mark" width="5" height="6"><path d="M.4 .4H4.6V5.4L2.5 4L.4 5.4Z" fill="none" stroke="var(--ink)" stroke-width=".6"/></svg>
    <div class="resp-text" style="top:24px;width:122px;line-height:7.4px"><b style="color:#5a5f74">During the interview</b>, you will likely be asked about specific work you've completed in relation to the position. <b style="color:#5a5f74">After reviewing the job description</b>, think of work you've done in past jobs, clubs or volunteer positions that show you have experience and success doing the work they require</div>
  </div>
</div>

<!-- My collections -->
<div class="phone" style="left:616px;top:508px">
  <div class="app-header" style="height:36px"><div class="back">‹</div><div class="screen-title">My collections</div></div>
  <div class="abs" style="left:0;top:36px;width:100%;height:30px;background:#fff"></div>
  <div class="search-bar"><svg width="6" height="6"><circle cx="2.5" cy="2.5" r="2" fill="none" stroke="var(--ink)" stroke-width=".9"/><path d="M4 4L5.8 5.8" stroke="var(--ink)" stroke-width=".9"/></svg>Search Questions and Tips</div>
  <div class="list-area" style="top:66px"></div>
  <div class="btn-ghost" style="left:10px;top:76px;font-size:4.8px;padding:0 8px">All categories ⌄</div>
  <div class="hint" style="top:100px;color:#6b7085">Select your question category</div>
  <div class="card" style="left:10px;top:108px;width:137px;height:45px"><div class="crumb abs" style="left:8px;top:5px">View Questions &amp; Responses › Behavioural</div><div class="q abs" style="left:8px;top:13px;width:112px">4. What parts of your current role frustrate you?</div><div class="delete" style="top:36px"><i></i>DELETE</div><span class="chev" style="top:17px">›</span></div>
  <div class="card" style="left:10px;top:160px;width:137px;height:45px"><div class="crumb abs" style="left:8px;top:5px">View Questions &amp; Responses › Behavioural</div><div class="q abs" style="left:8px;top:13px;width:112px">3. How would your colleagues describe you in three words?</div><div class="delete" style="top:36px"><i></i>DELETE</div><span class="chev" style="top:17px">›</span></div>
  <div class="card" style="left:10px;top:212px;width:137px;height:45px"><div class="crumb abs" style="left:8px;top:5px">Interview Tips › Tips Before the Interview</div><div class="q abs" style="left:8px;top:13px;width:112px">5. Recruit a friend to practice answering questions</div><div class="delete" style="top:36px"><i></i>DELETE</div><span class="chev" style="top:17px">›</span></div>
  <div class="card" style="left:10px;top:264px;width:137px;height:45px"><div class="crumb abs" style="left:8px;top:5px">Interview Tips › Tips Before the Interview</div><div class="q abs" style="left:8px;top:13px;width:112px">2. Practice your answers to common interview questions</div><div class="delete" style="top:36px;opacity:.6"><i></i>DELETE</div><span class="chev" style="top:17px">›</span></div>
</div>

<!-- Search -->
<div class="phone" style="left:804px;top:508px">
  <div class="app-header" style="height:36px"><div class="back">‹</div><div class="screen-title">Search</div></div>
  <div class="abs" style="left:0;top:36px;width:100%;height:30px;background:#fff"></div>
  <div class="search-bar"><svg width="6" height="6"><circle cx="2.5" cy="2.5" r="2" fill="none" stroke="var(--ink)" stroke-width=".9"/><path d="M4 4L5.8 5.8" stroke="var(--ink)" stroke-width=".9"/></svg>Search Questions and Tips</div>
  <div class="list-area" style="top:66px;height:270px"></div>
  <div class="art" role="img" aria-label="Illustration of a woman floating with a phone and a heart" style="left:22px;top:112px;width:113px;height:95px;border-radius:48% 52% 40% 60%;background:linear-gradient(150deg,#dfe4fd,#8194f2)"></div>
  <div class="abs" style="left:15px;top:224px;width:121px;text-align:center;font-family:'Poppins',sans-serif;font-weight:500;font-size:6.6px;line-height:10px;color:#7d8296">Anything good starts with a good questions</div>
</div>

<!-- Captions row 2 -->
<div class="caption" style="left:13px;top:864px">Interview Tips<span class="sub">Selection Menú</span></div>
<div class="caption" style="left:213px;top:864px">View Hints and Tips</div>
<div class="caption" style="left:401px;top:864px">View Hints and Tips - Hint 7</div>
<div class="caption" style="left:585px;top:864px">My question Portfolio<br>Saved Responses</div>
<div class="caption" style="left:780px;top:864px">Search section</div>

</body>
</html>
```